Tidal Brookfield ( New Product Range Office Furniture )

We are looking a dedicated page within our website www.quarnex.com.au ( must be Magento compatible ) to launch our new brand " TIDAL Brookfield "

We have our existing Brand "KEMO" has been selling in the last 10 years in Australia, We have just manufactured our new range please go our website and type "Tidal" in the search box.

The ideal is to have this page to showcase our new products in more professional manner, target audience is corporate customers.

We are also working with a office designers who they will use our website to show their clients with our products

Key Note
This web page is an additional page to be added to our existing website,

so WE DO NOT NEED SHOPPING CART in these pages,

Which means, when customer click on these pages, they will see a total corporate presentation of our Tidal Brookfield.

What we want to see is below

We want to showcase each product individually with main image with Long Description, because our product is a modular system we want to add thumbnail images to show 4 more different type of combination images (images to be provided later) so total of 5 images (we can live with 4 images if better spacing when design)

we need a good background theme to make sure they are all match nicely

Hope the above notes will help you get us a better design

Target Market(s)

Corporate End Users, Also Office Interior Designers

Industry/Entity Type

Office Furniture

Number of Pages Required

2 page

Font styles to use
Sans Serif

Requirements
Must have
• Our Tidal Brookfield product images ( can get from our website for now )
Nice to have
• Our Product Tidal Brookfield Range is a modular system, there are so many configuration that our customer can use to setup their office

```html
<!DOCTYPE html>
<html lang="en">
<head>
<meta charset="utf-8">
<title>Tidal Brookfield 1800 4-Door Hutch</title>
<link href="https://fonts.googleapis.com/css2?family=Jost:wght@400;500;600&family=Open+Sans:wght@400;600;700&display=swap" rel="stylesheet">
<style>
:root{
  --blue:#1283d6;
  --blue-bar:#0d86d4;
  --text:#333;
  --muted:#666;
  --line:#d9d9d9;
  --panel:#e4e4e4;
  --star:#f5b301;
  --help:#5c5e66;
  --avatar:#b3a189;
}
*{box-sizing:border-box;margin:0;padding:0}
html,body{width:1079px;height:1200px;overflow:hidden;background:#fff}
body{font-family:"Open Sans",Arial,sans-serif;color:var(--text);font-size:10px;letter-spacing:.3px}
.canvas{position:relative;width:1079px;height:1200px}
.abs{position:absolute}
.top-bar{left:0;top:0;width:1079px;height:10px;background:var(--blue-bar)}
.brand{left:184px;top:34px;display:flex;align-items:center;gap:10px}
.brand-mark{width:40px;height:40px;background:var(--blue)}
.brand-name{font-family:"Open Sans",sans-serif;font-size:38px;font-weight:700;color:#5b5b5b;letter-spacing:1px}
.hours{left:453px;top:42px;width:200px;text-align:right;line-height:12.5px;font-size:9.5px}
.account{left:713px;top:33px;display:flex;gap:14px;font-size:8.5px;text-transform:uppercase}
.search{left:713px;top:51px;width:197px;height:18px;border:1px solid #bbb;font-size:8.5px;padding:3px 6px;color:#444}
.search svg{position:absolute;right:6px;top:4px}
.rule{height:1px;background:var(--line)}
.nav{left:172px;top:113px;display:flex;gap:0;font-size:9.8px}
.nav span{margin-right:15px}
.nav span.dd:after{content:"";display:inline-block;margin-left:4px;border:3px solid transparent;border-top:4px solid #333;vertical-align:-1px}
.crumb{left:171px;top:147px;font-size:9.5px}
.crumb a{color:var(--blue);text-decoration:none}
.product-shot{left:176px;top:185px;width:220px;height:205px;background:linear-gradient(135deg,#a39a90,#6f6a66 60%,#3d3d3d);}
.zoom{left:241px;top:404px;font-size:9.5px;color:var(--muted);display:flex;gap:4px;align-items:center}
.label{font-size:9.5px;font-weight:600;color:var(--blue);text-transform:uppercase}
.thumbs{left:174px;top:466px;display:flex;gap:9px}
.thumb{width:50px;height:50px;border:1px solid #ccc;padding:6px}
.thumb div{width:100%;height:100%}
.t1{background:#3a3a3a}.t2{background:linear-gradient(#a69c90,#5a5a5a)}.t3{background:linear-gradient(#bcb2a6,#8b8178)}.t4{background:radial-gradient(ellipse at 50% 35%,#8a7d70 40%,#fff 42%)}
.divider-v{left:412px;top:169px;width:1px;height:346px;background:var(--line)}
.title{left:430px;top:167px;width:300px;font-family:"Jost",sans-serif;font-size:18.5px;font-weight:500;line-height:20px;color:#111;letter-spacing:.5px}
.title .nb{white-space:nowrap}
.rating-row{left:430px;top:216px;display:flex;gap:8px;align-items:center;font-size:9.8px;color:var(--blue)}
.rating-row .sep{color:#bbb}
.stars{color:var(--star);font-size:8px;letter-spacing:0}
.stars .off{color:#ccc}
.specs{left:430px;top:238px;display:grid;grid-template-columns:50px 100px 50px 90px;row-gap:4px;font-size:9px;line-height:11.5px}
.specs b{font-weight:600}
.desc{left:430px;top:308px;width:300px;font-size:9.5px;line-height:12.3px;color:var(--muted)}
.highlight{left:430px;top:375px;font-family:"Jost",sans-serif;font-size:13px;font-weight:500;color:var(--blue);letter-spacing:.5px}
.bullets{left:430px;top:400px;list-style:none;font-size:9.5px;line-height:19px}
.bullets li:before{content:"";display:inline-block;width:5px;height:5px;border-radius:50%;background:#333;margin-right:7px;vertical-align:1px}
.related{left:743px;top:169px;width:168px;height:331px;background:var(--panel)}
.related h3{position:absolute;left:10px;top:17px;font-family:"Jost",sans-serif;font-size:11px;font-weight:500;letter-spacing:.6px;color:#222}
.arrows{position:absolute;right:5px;top:16px;display:flex;gap:3px}
.arrows span{width:13px;height:13px;background:#fff;font-size:9px;line-height:13px;text-align:center}
.related-shot{position:absolute;left:40px;top:52px;width:88px;height:186px;background:linear-gradient(90deg,#2f2f2f 12%,#b5aba1 14%,#8e857c)}
.related p{position:absolute;left:0;top:256px;width:168px;text-align:center;font-family:"Jost",sans-serif;font-size:10.5px;font-weight:500;line-height:15px;color:#111}
.related .btn{position:absolute;left:39px;top:295px;width:90px;height:30px;border:1px solid #333;font-size:9.5px;line-height:28px;text-align:center;background:#fff}
.box{top:551px;width:234px;height:137px;border:1px solid #ccc;text-align:center}
.big{font-family:"Jost",sans-serif;font-size:29px;font-weight:500;color:var(--blue)}
.big small{font-size:14px;color:#888;font-weight:400}
.box .note{font-size:9.3px;color:var(--muted)}
.box a{color:var(--blue);text-decoration:none;font-size:9.5px}
.yn{position:absolute;top:92px;width:33px;height:20px;background:#e6e6e6;font-size:9.5px;line-height:20px;text-align:center;color:#222}
.review-btn{position:absolute;left:45px;top:79px;width:147px;height:28px;background:var(--blue);color:#fff;font-size:9.5px;font-weight:600;line-height:28px;letter-spacing:.5px}
.reviews-head{left:175px;top:728px;display:flex;gap:6px;align-items:center;font-family:"Jost",sans-serif;font-size:16.5px;font-weight:400;color:var(--blue);letter-spacing:.3px}
.reviews-head i{width:16px;height:16px;border:1.5px solid var(--blue);position:relative}
.reviews-head i:after{content:"";position:absolute;left:3px;right:3px;top:6px;height:1.5px;background:var(--blue)}
.avatar{width:31px;height:31px;border-radius:50%;background:var(--avatar);color:#fff;font-size:16px;font-weight:600;text-align:center;line-height:31px}
.review{left:239px;width:655px;font-size:9.6px;line-height:12.3px}
.review .stars{font-size:8px;display:block;margin-bottom:5px}
.review .by{display:block;margin-top:9px;color:var(--muted)}
.foot-h{top:996px;font-size:9.8px;font-weight:700;color:var(--blue);letter-spacing:.3px}
.foot-list{top:1013px;list-style:none;font-size:9.5px;line-height:14.8px}
.foot-list svg{vertical-align:-1px;margin-right:3px}
.badge{left:327px;top:1101px;width:152px;height:49px;background:#3a3a3a;border-radius:3px}
.news-text{left:658px;top:1014px;width:240px;font-size:9.5px;line-height:11.5px}
.news-input{left:658px;top:1051px;width:167px;height:23px;border:1px solid #bbb}
.news-btn{left:825px;top:1051px;width:63px;height:23px;background:var(--blue);color:#fff;font-size:8.5px;font-weight:600;text-align:center;line-height:23px;letter-spacing:.4px}
.help-shot{left:819px;top:1094px;width:69px;height:49px;background:linear-gradient(#e8e6e4,#2c2c30)}
.help{left:677px;top:1147px;width:236px;height:53px;background:var(--help);border-radius:3px 3px 0 0;color:#fff}
.help span{position:absolute;left:24px;top:20px;font-size:9.8px;font-weight:600}
.help .ctl{position:absolute;top:17px;width:22px;height:22px;background:#85878e;color:#fff;text-align:center;line-height:22px;font-size:13px;font-weight:700}
.copy{left:174px;top:1179px;font-size:9.5px}
</style>
</head>
<body>
<div class="canvas">
  <div class="abs top-bar"></div>

  <header>
    <div class="abs brand"><span class="brand-mark"></span><span class="brand-name">QUARNEX</span></div>
    <div class="abs hours">Monday - Friday : 8.30AM - 5PM<br>Saturday : 9AM - 3PM<br>Sundays &amp; Public Holidays : Closed</div>
    <div class="abs account"><span>My Account</span><span>Compare</span><span>Log In</span><span>Sign Up</span></div>
    <div class="abs search">Search for a product...
      <svg width="9" height="9" viewBox="0 0 10 10"><circle cx="4" cy="4" r="3" fill="none" stroke="#222" stroke-width="1.5"/><path d="M6.3 6.3L9 9" stroke="#222" stroke-width="1.6"/></svg>
    </div>
    <div class="abs rule" style="left:167px;top:105px;width:745px"></div>
    <nav class="abs nav">
      <span class="dd">Desking</span><span class="dd">Seating</span><span class="dd">Storage</span><span class="dd">Screens</span><span class="dd" style="margin-left:4px">Tables</span><span class="dd" style="margin-left:4px">Reception Counters</span><span class="dd" style="margin-left:3px">Accessories</span><span style="margin-left:2px">Quality Second Hand</span><span class="dd">Choose Your Workshop</span>
    </nav>
    <div class="abs rule" style="left:167px;top:135px;width:745px"></div>
  </header>

  <div class="abs crumb"><a href="#">Home</a> / Tidal Brookfield 1500 3-Door Hutch</div>

  <section class="product">
    <div class="abs product-shot" role="img" aria-label="Tidal Brookfield 1800 4-door hutch in linewood finish"></div>
    <div class="abs zoom"><svg width="8" height="8" viewBox="0 0 10 10"><circle cx="4" cy="4" r="3" fill="none" stroke="#666" stroke-width="1.5"/><path d="M6.3 6.3L9 9" stroke="#666" stroke-width="1.6"/></svg>Hover to zoom</div>
    <div class="abs label" style="left:174px;top:449px">Combinations</div>
    <div class="abs thumbs">
      <div class="thumb"><div class="t1" role="img" aria-label="Desk combination"></div></div>
      <div class="thumb"><div class="t2" role="img" aria-label="Credenza combination"></div></div>
      <div class="thumb"><div class="t3" role="img" aria-label="Drawer unit combination"></div></div>
      <div class="thumb"><div class="t4" role="img" aria-label="Round meeting table combination"></div></div>
    </div>
    <div class="abs divider-v"></div>

    <h1 class="abs title">TIDAL BROOKFIELD 1800 <span class="nb">4-DOOR</span> HUTCH</h1>
    <div class="abs rating-row"><span class="stars">★★★★<span class="off">★</span></span><span>4.2 ratings</span><span class="sep">|</span><span>25 reviews</span><span class="sep">|</span><span>View Q &amp; A</span></div>
    <div class="abs specs">
      <b>POS SKU</b><span>QTBH18LW</span><b>Depth</b><span>380mm</span>
      <b>Height</b><span>1070mm</span><b>Colour</b><span>Ashen/Slate</span>
      <b>Width</b><span>1800mm</span>
    </div>
    <div class="abs rule" style="left:422px;top:294px;width:299px"></div>
    <p class="abs desc">Bring the Tidal 1800 4-Door Hutch into your office and forget all of your storage problems. Combine this high quality hutch with a desk or credenza to create a complete workstation for your office.</p>
    <h2 class="abs highlight">PRODUCT HIGHLIGHT</h2>
    <ul class="abs bullets">
      <li>Soft Textured Melamine Surfaces</li>
      <li>Soft Close Doors</li>
      <li>E1 Melamine Board (Australian Standard)</li>
      <li>Features 25mm tops and ABS edging</li>
      <li>Dimensions: 1800L x 380W x 1070H mm</li>
      <li>Comes with a 10 Year Warranty</li>
    </ul>

    <aside class="abs related">
      <h3>RELATED PRODUCTS</h3>
      <div class="arrows"><span>‹</span><span>›</span></div>
      <div class="related-shot" role="img" aria-label="Tidal Brookfield filing cabinet with 4 drawers"></div>
      <p>TIDAL BROOKFIELD FILING<br>CABINET 4 DRAWERS</p>
      <div class="btn">View Product</div>
    </aside>
  </section>

  <div class="abs rule" style="left:167px;top:535px;width:745px"></div>

  <section class="summary">
    <div class="abs box" style="left:168px">
      <div class="big" style="margin-top:18px">4.2<small> /5</small></div>
      <div class="stars" style="margin-top:1px">★★★★<span class="off">★</span></div>
      <div class="note" style="margin-top:3px">4.2 Ratings &amp; 25 Reviews</div>
      <div style="margin-top:9px"><a href="#">View All Reviews</a></div>
    </div>
    <div class="abs box" style="left:423px">
      <div class="big" style="margin-top:18px">67%</div>
      <div class="note" style="margin-top:2px">Based on 20 Recommendations.</div>
      <div class="note" style="position:absolute;left:18px;top:90px;text-align:left;line-height:12px">Would you like to<br>recommend this item?</div>
      <div class="yn" style="left:155px">YES</div>
      <div class="yn" style="left:193px">NO</div>
    </div>
    <div class="abs box" style="left:678px">
      <div class="note" style="margin-top:35px;line-height:13.5px;color:#444">Have you used this product?<br>Please give us a review</div>
      <div class="review-btn">REVIEW</div>
    </div>
  </section>

  <div class="abs rule" style="left:167px;top:706px;width:745px"></div>

  <section class="reviews">
    <h2 class="abs reviews-head"><i></i>Customer reviews</h2>
    <div class="abs avatar" style="left:191px;top:767px">A</div>
    <div class="abs review" style="top:764px"><span class="stars">★★★★★</span>Lorem ipsum dolor sit amet, consectetur adipiscing elit, sed do eiusmod tempor incididunt ut labore et dolore magna aliqua. Ut enim ad minim veniam, quis nostrud exercitation ullamco laboris nisi ut aliquip ex ea commodo consequat. Duis aute irure dolor in repreh enderit in voluptate velit esse cillum.<span class="by">by Arjun on Sep 03, 2016</span></div>
    <div class="abs avatar" style="left:191px;top:865px">M</div>
    <div class="abs review" style="top:864px"><span class="stars">★★★★★</span>Lorem ipsum dolor sit amet, consectetur adipiscing elit, sed do eiusmod tempor incididunt ut labore et dolore magna aliqua. Ut enim ad minim veniam, quis nostrud exercitation ullamco laboris nisi ut aliquip ex ea commodo consequat. Duis aute irure dolor in repreh enderit in voluptate velit esse cillum.<span class="by">by Miles on May 15, 2016</span></div>
  </section>

  <div class="abs rule" style="left:167px;top:963px;width:745px"></div>

  <footer>
    <h4 class="abs foot-h" style="left:176px">CATEGORIES</h4>
    <ul class="abs foot-list" style="left:176px"><li>Desking</li><li>Drawers</li><li>Seating</li><li>Storage</li><li>Screens</li><li>Tables</li><li>Reception Corners</li><li>Accessories</li><li>Second Hand</li></ul>
    <h4 class="abs foot-h" style="left:327px">CUSTOMER CARE</h4>
    <ul class="abs foot-list" style="left:327px"><li>About Us</li><li>Privacy Policy</li><li>Shipping &amp; Returns</li><li>Testimonials</li><li>My Account</li></ul>
    <div class="abs badge" role="img" aria-label="Secure payment badge"></div>
    <h4 class="abs foot-h" style="left:478px">CUSTOMER CARE</h4>
    <ul class="abs foot-list" style="left:478px">
      <li><svg width="8" height="9" viewBox="0 0 10 12"><path d="M5 0a4 4 0 0 0-4 4c0 3 4 8 4 8s4-5 4-8a4 4 0 0 0-4-4z" fill="#1283d6"/><circle cx="5" cy="4" r="1.5" fill="#fff"/></svg>27 Harlow Street</li>
      <li style="padding-left:13px">Kelmscott</li>
      <li style="padding-left:13px">Western Australia</li>
      <li><svg width="8" height="9" viewBox="0 0 10 10"><path d="M2 0l2 2-1 2c1 1.5 2 2.5 3 3l2-1 2 2-2 2C4 10 0 6 0 2z" fill="#1283d6"/></svg>(08) 9123 4567</li>
      <li><svg width="9" height="8" viewBox="0 0 12 9"><rect width="12" height="9" fill="#1283d6"/><path d="M0 0l6 5 6-5" fill="none" stroke="#fff"/></svg>info@quarnexgroup.com.au</li>
    </ul>
    <h4 class="abs foot-h" style="left:658px">WANT THE LATEST DEALS?</h4>
    <p class="abs news-text">Sign up to our newsletter and receive 10% off your next purchase!</p>
    <div class="abs news-input"></div>
    <div class="abs news-btn">SUBSCRIBE</div>
    <div class="abs help-shot" role="img" aria-label="Customer support team"></div>
    <div class="abs help"><span>NEED HELP? We're here!</span><div class="ctl" style="left:176px;font-size:9px">▼</div><div class="ctl" style="left:202px">+</div></div>
    <div class="abs copy">Copyright © Quarnex 2016</div>
  </footer>
</div>
</body>
</html>
```